TriVex Business Card Design - double sided -plumbing local plumbing company

We have a Plumbing company where the design was create through Sketch Hive. We would now like a business card designed as well. We want it to be in the colour version of the logo.

Details below for the card.

Phone Number: 0438 615 247
Email: info@trivexplumbing.example.au
Website: https://trivexplumbing.example.au
We really want a sophisticated design that stand out from the other- informative and timeless.

Target Market(s)

local Canberra market

Industry/Entity Type

Plumbing, gas fitting, hot water

Contact Information for Business Card

Phone number, email, logo and "Supplying all your heating, cooling and hot water needs"

Requirements
Must have
• bust be colourful, must also be though about it being printed on a magnet. must Vex with the logo - I dont want the logo and information chucked onto a white canvas I would prefer it to be smooth and look purposeful

```html
<!DOCTYPE html>
<html lang="en">
<head>
<meta charset="utf-8">
<title>TriVex Plumbing – Business Card</title>
<link href="https://fonts.googleapis.com/css2?family=Arimo:wght@400;700&display=swap" rel="stylesheet">
<style>
  :root {
    --canvas: #e8e8e8;
    --card-front: #ffffff;
    --brand-blue: #1aa3e0;
    --brand-orange: #fbb040;
    --ink: #111111;
    --white: #ffffff;
  }
  * { box-sizing: border-box; margin: 0; padding: 0; }
  html, body {
    width: 1200px;
    height: 1200px;
    overflow: hidden;
    background: var(--canvas);
    font-family: "Arimo", Arial, sans-serif;
  }
  .card {
    position: absolute;
    left: 150px;
    width: 900px;
    height: 527px;
    box-shadow: 4px 6px 10px rgba(0,0,0,0.18);
  }
  .card--front { top: 54px; background: var(--card-front); }
  .card--back { top: 625px; background: var(--brand-orange); }

  .brand {
    position: absolute;
    left: 0;
    right: 0;
    display: flex;
    flex-direction: column;
    align-items: center;
  }
  .card--front .brand { top: 88px; color: var(--brand-blue); }
  .card--back .brand { top: 188px; color: var(--white); }
  .brand__mark {
    display: flex;
    align-items: center;
    gap: 20px;
    height: 100px;
  }
  .brand__name {
    font-size: 104px;
    font-weight: 700;
    letter-spacing: 2px;
    line-height: 1;
  }
  .brand__dot {
    width: 32px;
    height: 32px;
    border-radius: 50%;
    background: currentColor;
  }
  .brand__descriptor {
    margin-top: 16px;
    padding-left: 12px;
    font-size: 31px;
    font-weight: 700;
    letter-spacing: 12px;
    line-height: 1;
    text-transform: uppercase;
  }
  .tagline {
    position: absolute;
    left: 0;
    right: 0;
    top: 392px;
    text-align: center;
    font-size: 22px;
    color: var(--white);
    letter-spacing: 0.5px;
  }

  .contact {
    position: absolute;
    left: 0;
    right: 0;
    top: 318px;
    display: flex;
    flex-direction: column;
    align-items: center;
    color: var(--ink);
  }
  .contact__phone-icon {
    width: 45px;
    height: 45px;
    border-radius: 7px;
    background: var(--brand-orange);
    display: flex;
    align-items: center;
    justify-content: center;
  }
  .contact__phone {
    margin-top: 20px;
    font-size: 30px;
    font-weight: 700;
    letter-spacing: 0.5px;
  }
  .contact__line {
    margin-top: 18px;
    display: flex;
    align-items: center;
    gap: 14px;
    font-size: 23px;
  }
  .contact__icon { display: block; }
</style>
</head>
<body>
  <section class="card card--front" aria-label="Business card front">
    <div class="brand">
      <div class="brand__mark">
        <span class="brand__name">TriVex</span>
        <span class="brand__dot"></span>
      </div>
      <span class="brand__descriptor">Plumbing</span>
    </div>
    <div class="contact">
      <div class="contact__phone-icon">
        <svg class="contact__icon" width="22" height="22" viewBox="0 0 24 24" aria-hidden="true">
          <path fill="#ffffff" d="M6.6 10.8c1.4 2.8 3.8 5.1 6.6 6.6l2.2-2.2c.3-.3.7-.4 1-.2 1.1.4 2.3.6 3.6.6.6 0 1 .4 1 1V20c0 .6-.4 1-1 1C10.6 21 3 13.4 3 4c0-.6.4-1 1-1h3.5c.6 0 1 .4 1 1 0 1.3.2 2.5.6 3.6.1.3 0 .7-.2 1L6.6 10.8z"/>
        </svg>
      </div>
      <div class="contact__phone">0438 615 247</div>
      <div class="contact__line">
        <svg class="contact__icon" width="18" height="14" viewBox="0 0 18 14" aria-hidden="true">
          <rect x="0" y="0" width="18" height="14" rx="2" fill="#111111"/>
          <path d="M1.5 2 L9 7.5 L16.5 2" fill="none" stroke="#ffffff" stroke-width="1.6"/>
        </svg>
        <span>info@trivexplumbing.example.au | trivexplumbing.example.au</span>
        <svg class="contact__icon" width="18" height="18" viewBox="0 0 20 20" aria-hidden="true">
          <g fill="none" stroke="#111111" stroke-width="1.6">
            <circle cx="10" cy="10" r="8.5"/>
            <ellipse cx="10" cy="10" rx="3.8" ry="8.5"/>
            <line x1="1.5" y1="10" x2="18.5" y2="10"/>
          </g>
        </svg>
      </div>
    </div>
  </section>

  <section class="card card--back" aria-label="Business card back">
    <div class="brand">
      <div class="brand__mark">
        <span class="brand__name">TriVex</span>
        <span class="brand__dot"></span>
      </div>
      <span class="brand__descriptor">Plumbing</span>
    </div>
    <p class="tagline">Supplying all your heating, cooling and hot water needs</p>
  </section>
</body>
</html>
```